A5 Flyer for mobile App development

We need a double sided flyer design that will need to be printed on A5 sized paper.
The design will be based on a phone/tablet look and feel.

The idea behind the pamphlet is that we show clients that they can have a mobile app white labelled to their company/brand.

The front of the pamphlet will need to look like a front of a phone with a generic mobile app running within the phone.
The phone must not resemble a real phone, however, it should resemble a cartoon look phone - similar to the attached image called "phone.jpg". The mobile app running within the phone needs to have a "drawing/wireframe" look - similar to the "mock.jpg" image attached. The logo part should look like a "placeholder" image - similar to the image named "mocklogo" (look at the far left) attached.

The back of the pamphlet must also be similar, so that when you turn over the pamphlet, it should look like you're turning over a real phone, and you're now the seeing the back of the phone.
The back of the phone should be styled similar to the front. The text and items on the back of the phone are also in the image named "20170503_212415.jpg".

The phone on the pamphlet should not have an outline, meaning that the pamphlet will have rounded corners, giving the phone a shape.

Please send us a message if you're unsure about anything.

Target Market(s)

Businesses that have salons, spa's, beauty clinics, etc.

Industry/Entity Type

Health And Wellness

Font styles to use
Sans Serif
Script

Colors
e34297

Requirements
Must have
• The pamphlet will have rounded corners, giving the phone its look. See attached the image named "pingloom.."
Should not have
• the phone on the pamphlet should not have an outline, meaning that the pamphlet will have rounded corners, giving the phone a shape. Please have a look at the pingloom image attached that demonstrates the cut out lines.

```html
<!DOCTYPE html>
<html lang="en">
<head>
<meta charset="utf-8">
<title>App Flyer – Front and Back</title>
<link rel="stylesheet" href="https://fonts.googleapis.com/css2?family=Nunito:wght@300;400;700;800&family=Comic+Neue:wght@700&display=swap">
<style>
  :root {
    --paper: #ffffff;
    --phone-body: #000000;
    --brand-pink: #e34297;
    --screen-top: #ffffff;
    --placeholder-bg: #c8c8c8;
    --placeholder-mark: #8f8f8f;
    --logo-box: #d4d4d4;
    --cta-green: #8cc43f;
    --ink-light: #ffffff;
    --ink-dark: #111111;
  }
  * { box-sizing: border-box; margin: 0; padding: 0; }
  html, body {
    width: 1200px; height: 804px; overflow: hidden;
    background: var(--paper);
    font-family: "Nunito", sans-serif;
  }
  .canvas { position: relative; width: 1200px; height: 804px; }

  .phone {
    position: absolute; top: 15px; height: 771px;
    background: var(--phone-body);
  }
  .phone--front { left: 13px; width: 537px; }
  .phone--back  { left: 643px; width: 538px; }

  /* Front */
  .earpiece {
    position: absolute; left: 245px; top: 41px;
    width: 46px; height: 7px; border-radius: 4px; background: var(--ink-light);
  }
  .front-camera {
    position: absolute; left: 330px; top: 39px;
    width: 10px; height: 10px; border-radius: 50%; background: var(--ink-light);
  }
  .screen {
    position: absolute; left: 13px; top: 57px; width: 510px; height: 658px;
    background: linear-gradient(to bottom, var(--screen-top) 0%, #f3c3de 20%, #ea86bb 40%, var(--brand-pink) 60%, var(--brand-pink) 100%);
    overflow: hidden;
  }
  .logo-placeholder {
    position: absolute; left: 192px; top: 25px; width: 125px; height: 125px;
    background: var(--placeholder-bg);
  }
  .logo-placeholder::after {
    content: ""; position: absolute; left: 26px; top: 26px;
    width: 73px; height: 73px; border-radius: 50%; background: var(--placeholder-mark);
  }
  .brand-slider {
    position: absolute; left: 32px; top: 214px; width: 440px; height: 300px;
    border: 2px solid var(--ink-light); border-radius: 13px;
  }
  .brand-slider__title {
    position: absolute; left: 0; right: 0; top: 94px;
    text-align: center; color: var(--ink-light);
    font-weight: 800; font-size: 41px; line-height: 54px;
  }
  .slider-arrow { position: absolute; top: 120px; width: 32px; height: 60px; }
  .slider-arrow--prev { left: 16px; }
  .slider-arrow--next { right: 16px; }
  .cta-button {
    position: absolute; left: 32px; top: 562px; width: 440px; height: 91px;
    border-radius: 11px; background: var(--cta-green);
  }
  .home-button {
    position: absolute; left: 248px; top: 723px; width: 41px; height: 41px;
    border-radius: 50%; background: var(--ink-light);
  }
  .home-button::after {
    content: ""; position: absolute; left: 13px; top: 13px; width: 15px; height: 15px;
    border: 3px solid var(--phone-body); border-radius: 5px;
  }

  /* Back */
  .rear-camera {
    position: absolute; left: 234px; top: 110px; width: 70px; height: 70px;
    background: var(--ink-light);
  }
  .rear-flash {
    position: absolute; left: 317px; top: 136px; width: 18px; height: 18px;
    border-radius: 50%; background: var(--ink-light);
  }
  .client-logo {
    position: absolute; left: 152px; top: 231px; width: 232px; height: 70px;
    background: var(--logo-box); color: var(--ink-dark);
    display: flex; align-items: center; justify-content: center; text-align: center;
    font-weight: 700; font-size: 21px; line-height: 27px;
  }
  .price {
    position: absolute; left: 0; right: 0; top: 355px; text-align: center;
    font-family: "Comic Neue", cursive; font-weight: 700; font-size: 54px;
    color: var(--ink-light);
  }
  .pitch {
    position: absolute; left: 0; right: 0; top: 445px; text-align: center;
    color: var(--ink-light); text-transform: uppercase;
    font-weight: 300; font-size: 29px; line-height: 38.5px; letter-spacing: 0.5px;
  }
  .pitch strong { font-weight: 800; }
  .platforms {
    position: absolute; left: 0; right: 0; top: 628px;
    display: flex; justify-content: center; gap: 46px;
    color: var(--ink-light); font-weight: 700; font-size: 38px;
  }
</style>
</head>
<body>
<main class="canvas">
  <section class="phone phone--front" aria-label="Flyer front">
    <span class="earpiece"></span>
    <span class="front-camera"></span>
    <div class="screen">
      <div class="logo-placeholder" aria-label="Logo placeholder"></div>
      <div class="brand-slider">
        <svg class="slider-arrow slider-arrow--prev" viewBox="0 0 32 60" aria-hidden="true">
          <polyline points="30,2 2,30 30,58" fill="none" stroke="#fff" stroke-width="2"/>
        </svg>
        <p class="brand-slider__title">Your Brand<br>Here</p>
        <svg class="slider-arrow slider-arrow--next" viewBox="0 0 32 60" aria-hidden="true">
          <polyline points="2,2 30,30 2,58" fill="none" stroke="#fff" stroke-width="2"/>
        </svg>
      </div>
      <div class="cta-button"></div>
    </div>
    <span class="home-button"></span>
  </section>

  <section class="phone phone--back" aria-label="Flyer back">
    <span class="rear-camera"></span>
    <span class="rear-flash"></span>
    <div class="client-logo">My #Glow<br>Logo</div>
    <p class="price">From 499rm</p>
    <p class="pitch">Let your clients book<br>their next appointment<br><strong>using your app</strong></p>
    <div class="platforms">
      <span class="platform">Nimbus</span>
      <span class="platform">Orbit</span>
    </div>
  </section>
</main>
</body>
</html>
```